Orbit 582 - Kindle Book Cover

I am looking for a Kindle book cover for my book about "Orbit 582".
The Book is Titled:
Orbit 582 Ascended
Shaping Tomorrow: Paths To Unlocking Hidden Currents
Author is Dorian Welby
Here is a book description that may help you understand more about it:
Inspired by the genius of Bertram Ollinger, this comprehensive guide delves into the ancient wisdom and cutting-edge science behind the 582 method, a powerful tool for manifesting your desires. Whether you're seeking personal growth, financial success, or spiritual enlightenment, this book provides advanced techniques and methods to transform your dreams into reality.
Any questions please ask.
Thanks
Gavin

```html
<!DOCTYPE html>
<html lang="en">
<head>
<meta charset="utf-8">
<title>Orbit 582 Ascended — Dorian Welby</title>
<link rel="stylesheet" href="https://fonts.googleapis.com/css2?family=Abril+Fatface&family=Old+Standard+TT:wght@400&display=swap">
<style>
  :root {
    --space-deep: #03161a;
    --space-teal: #0b3a40;
    --nebula-teal: #16585e;
    --glow-cyan: #2ad6cc;
    --glow-aqua: #1fb5a8;
    --glow-green: #22b05e;
    --floor-green: #062a16;
    --ink-white: #ffffff;
  }
  html, body {
    margin: 0;
    padding: 0;
    width: 800px;
    height: 1200px;
    overflow: hidden;
    background: var(--space-deep);
  }
  .cover {
    position: relative;
    width: 800px;
    height: 1200px;
    overflow: hidden;
  }
  .cover-art {
    position: absolute;
    inset: 0;
    background:
      radial-gradient(ellipse 38% 22% at 22% 72%, rgba(42,214,204,0.55), rgba(42,214,204,0) 75%),
      radial-gradient(ellipse 34% 22% at 80% 74%, rgba(42,214,204,0.45), rgba(42,214,204,0) 75%),
      radial-gradient(ellipse 30% 26% at 50% 78%, rgba(31,181,168,0.55), rgba(31,181,168,0) 75%),
      radial-gradient(ellipse 55% 18% at 50% 100%, rgba(34,176,94,0.85), rgba(34,176,94,0) 80%),
      radial-gradient(ellipse 30% 15% at 10% 96%, rgba(34,176,94,0.6), rgba(34,176,94,0) 80%),
      radial-gradient(ellipse 30% 15% at 90% 96%, rgba(34,176,94,0.6), rgba(34,176,94,0) 80%),
      radial-gradient(ellipse 25% 14% at 75% 44%, rgba(40,120,125,0.45), rgba(40,120,125,0) 75%),
      radial-gradient(ellipse 40% 20% at 35% 12%, rgba(22,88,94,0.55), rgba(22,88,94,0) 75%),
      linear-gradient(180deg, #06262b 0%, var(--space-teal) 30%, #0c3f44 50%, #0f5552 65%, #0d5040 82%, var(--floor-green) 100%);
  }
  .title {
    position: absolute;
    left: 0;
    right: 0;
    top: 143px;
    margin: 0;
    text-align: center;
    font-family: "Abril Fatface", "Playfair Display", serif;
    font-weight: 400;
    font-size: 90px;
    line-height: 100px;
    letter-spacing: 3px;
    color: var(--ink-white);
    text-transform: uppercase;
  }
  .subtitle {
    position: absolute;
    left: 40px;
    right: 40px;
    top: 357px;
    margin: 0;
    text-align: center;
    font-family: "Old Standard TT", "Times New Roman", serif;
    font-weight: 400;
    font-size: 44px;
    line-height: 51px;
    letter-spacing: 1px;
    color: var(--ink-white);
  }
  .author {
    position: absolute;
    left: 0;
    right: 0;
    top: 1078px;
    margin: 0;
    text-align: center;
    font-family: "Old Standard TT", "Times New Roman", serif;
    font-weight: 400;
    font-size: 31px;
    letter-spacing: 1px;
    color: var(--ink-white);
    text-transform: uppercase;
  }
</style>
</head>
<body>
  <main class="cover">
    <div class="cover-art" role="img" aria-label="Deep teal starfield with glowing cyan and green light streaks bursting upward from the bottom"></div>
    <h1 class="title">Orbit 582<br>Ascended</h1>
    <p class="subtitle">Shaping Tomorrow: Paths to Unlocking Hidden Currents</p>
    <p class="author">Dorian Welby</p>
  </main>
</body>
</html>
```